LOGO DESIGN: Construction Related Service Business

We require a logo for our business Dovtar Services. We are a construction related business offering a range of services including machine services for groundworks (digging trenches, soak wells, preparing land for construction etc), demolition and truck haulage from demolition sites.
We would like our logo to be predominately text, but may include abstract graphics. The colour scheme should be mainly a mid bright blue and overall be quite 'clean'.

Industry/Entity Type

Construction

Contact Information for Business Card

Colin Pruett
Ph:041 562 9083
dovtarservices@keloran.com.au

Colors
0456a3

```html
<!DOCTYPE html>
<html lang="en">
<head>
<meta charset="utf-8">
<title>Dovtar Services — Business Card</title>
<link rel="stylesheet" href="https://fonts.googleapis.com/css2?family=Questrial&display=swap">
<style>
  :root {
    --brand-blue: #1d5699;
    --card-white: #ffffff;
    --card-shade: #ececec;
    --backdrop: #e6e8eb;
  }
  html, body {
    margin: 0;
    padding: 0;
    width: 1200px;
    height: 848px;
    overflow: hidden;
    background: var(--backdrop);
  }
  .canvas {
    position: relative;
    width: 1200px;
    height: 848px;
  }
  .business-card {
    position: absolute;
    left: 158px;
    top: 137px;
    width: 876px;
    height: 537px;
    border-radius: 26px;
    background: radial-gradient(ellipse at 65% 25%, var(--card-white) 0%, var(--card-white) 40%, var(--card-shade) 100%);
    box-shadow: 0 3px 8px rgba(0, 0, 0, 0.25);
    font-family: "Questrial", sans-serif;
    color: var(--brand-blue);
  }
  .brand-name {
    position: absolute;
    left: 142px;
    top: 78px;
    margin: 0;
    font-weight: 400;
    font-size: 158px;
    line-height: 1;
    letter-spacing: 4px;
  }
  .brand-tagline {
    position: absolute;
    left: 368px;
    top: 292px;
    margin: 0;
    font-weight: 400;
    font-size: 39px;
    line-height: 1;
    letter-spacing: 25px;
  }
  .contact-line {
    position: absolute;
    left: 18px;
    top: 480px;
    margin: 0;
    font-size: 25px;
    letter-spacing: 0.8px;
    white-space: pre;
  }
</style>
</head>
<body>
  <main class="canvas">
    <section class="business-card" aria-label="Dovtar Services business card">
      <h1 class="brand-name">DOVTAR</h1>
      <p class="brand-tagline">SERVICES</p>
      <p class="contact-line">Colin Pruett / ph:041 562 9083 /  dovtarservices@keloran.com.au</p>
    </section>
  </main>
</body>
</html>
```